Artisan Bread Company needs a business card

I need a business card design, for an artisan bread company called "Holloway's Bread".

I would like the logo on one side, and on the other, I would like it to say

Dorian Holloway
Baker
416.552.0193
hollowaysbread@breadmail.example

Not necessarily in that order- but it must have these.

Industry/Entity Type

Business

Font styles to use
Serif

Requirements
Must have
• The provided logo on the front, this on the back-
• Dorian Holloway
• Baker
• 416.552.0193
• hollowaysbread@breadmail.example

```html
<!DOCTYPE html>
<html lang="en">
<head>
<meta charset="utf-8">
<title>Holloway's Bread — Business Card</title>
<link href="https://fonts.googleapis.com/css2?family=Tinos&family=Arimo&family=Federo&display=swap" rel="stylesheet">
<style>
  :root {
    --page: #1e1e1e;
    --paper: #f1f1f1;
    --espresso: #211a1f;
    --amber: #d98a1e;
    --gold: #b8892f;
    --gold-light: #e0b955;
    --ink-light: #f4f1ee;
  }
  * { box-sizing: border-box; margin: 0; padding: 0; }
  html, body { width: 1200px; height: 800px; overflow: hidden; }
  body { background: var(--page); position: relative; }

  .card {
    position: absolute;
    top: 238px;
    width: 536px;
    height: 306px;
    overflow: hidden;
  }
  .card--front { left: 49px; background: var(--espresso); }
  .card--back { left: 617px; background: var(--paper); display: flex; }

  .front__top-band { position: absolute; left: 0; top: 0; width: 100%; height: 91px; background: var(--paper); }
  .front__base-band { position: absolute; left: 0; bottom: 0; width: 100%; height: 26px; background: var(--amber); }

  .gallery { position: absolute; top: 56px; left: 105px; display: flex; gap: 14px; }
  .gallery__frame {
    width: 99px; height: 86px;
    padding: 5px;
    background: linear-gradient(135deg, var(--gold-light), var(--gold) 50%, var(--gold-light));
  }
  .gallery__mat { width: 100%; height: 100%; background: #111; padding: 5px; }
  .gallery__photo { width: 100%; height: 100%; }
  .gallery__photo--pastry { background: linear-gradient(135deg, #e7cf9a, #c05a4a 60%, #f0e6d8); }
  .gallery__photo--pie { background: linear-gradient(135deg, #9ab05a, #d9b36a 55%, #e9e2d2); }
  .gallery__photo--sandwich { background: linear-gradient(135deg, #e8d8b8, #c9a46a 55%, #d0362a 85%); }

  .identity { position: absolute; top: 163px; width: 100%; text-align: center; color: var(--ink-light); }
  .identity__name { font-family: "Tinos", serif; font-size: 31px; line-height: 1; font-weight: 400; }
  .identity__role { font-family: "Federo", "Tinos", serif; font-size: 20px; line-height: 1.1; letter-spacing: 0.5px; }

  .contact {
    position: absolute; top: 236px; left: 15px; right: 15px;
    display: flex; align-items: center;
    color: var(--ink-light); font-family: "Arimo", sans-serif;
  }
  .contact__email { font-size: 14.5px; white-space: nowrap; }
  .contact__icon { width: 13px; height: 11px; flex: none; margin-left: 10px; }
  .contact__icon--phone { margin-left: 24px; }
  .contact__phone { margin-left: 10px; font-size: 17px; white-space: nowrap; }

  .back__strip { height: 100%; border-right: 1px solid #e6e2dc; }
  .back__strip:last-of-type { border-right: none; }
  .back__strip--cake { width: 97px; background: linear-gradient(180deg, #e4dcd4, #d8cbbf 50%, #e7e0d8); }
  .back__strip--roll { width: 105px; background: linear-gradient(180deg, #f3ebd8, #efdcb4 45%, #f4eee0); }
  .back__strip--burger { width: 105px; background: linear-gradient(180deg, #efe4d2, #e9c9ae 50%, #ece2d4); }
  .back__strip--grain { width: 105px; background: linear-gradient(180deg, #f2ece0, #e7dcc8 50%, #f0ece6); }
  .back__strip--loaf { width: 124px; background: linear-gradient(180deg, #f0ece6, #ecdcbc 45%, #e2dbd2); }

  .brand {
    position: absolute; left: 0; top: 0; width: 100%; height: 100%;
    display: flex; align-items: center; justify-content: center; gap: 14px;
  }
  .brand__mark { width: 18px; height: 18px; border-radius: 50%; background: var(--espresso); flex: none; }
  .brand__name { font-family: "Tinos", serif; font-size: 42px; font-weight: 400; color: var(--espresso); line-height: 1; }
</style>
</head>
<body>
  <section class="card card--front">
    <div class="front__top-band"></div>
    <div class="gallery">
      <div class="gallery__frame"><div class="gallery__mat"><div class="gallery__photo gallery__photo--pastry" role="img" aria-label="Photo of a fruit-topped pastry"></div></div></div>
      <div class="gallery__frame"><div class="gallery__mat"><div class="gallery__photo gallery__photo--pie" role="img" aria-label="Photo of a savoury pie with greens"></div></div></div>
      <div class="gallery__frame"><div class="gallery__mat"><div class="gallery__photo gallery__photo--sandwich" role="img" aria-label="Photo of a sandwich with tomatoes"></div></div></div>
    </div>
    <div class="identity">
      <h1 class="identity__name">Dorian Holloway</h1>
      <p class="identity__role">Baker</p>
    </div>
    <div class="contact">
      <span class="contact__email">hollowaysbread@breadmail.example</span>
      <svg class="contact__icon" viewBox="0 0 13 11"><rect width="13" height="11" fill="#f4f1ee"/><path d="M2 3 L6.5 6.5 L11 3" stroke="#211a1f" stroke-width="1.2" fill="none"/></svg>
      <svg class="contact__icon contact__icon--phone" viewBox="0 0 13 11"><rect width="13" height="11" fill="#f4f1ee"/><path d="M3 4.5 Q6.5 1.5 10 4.5 L9 5.5 L7.5 4.5 L5.5 4.5 L4 5.5 Z" fill="#211a1f"/><rect x="4.5" y="6" width="4" height="3" fill="#211a1f"/></svg>
      <span class="contact__phone">416.552.0193</span>
    </div>
    <div class="front__base-band"></div>
  </section>

  <section class="card card--back">
    <div class="back__strip back__strip--cake" role="img" aria-label="Faded photo of a decorated chocolate cake"></div>
    <div class="back__strip back__strip--roll" role="img" aria-label="Faded photo of a bread roll with grated cheese"></div>
    <div class="back__strip back__strip--burger" role="img" aria-label="Faded photo of a sandwich with tomato and basil"></div>
    <div class="back__strip back__strip--grain" role="img" aria-label="Faded photo of grains and flour"></div>
    <div class="back__strip back__strip--loaf" role="img" aria-label="Faded photo of a loaf with olives"></div>
    <div class="brand">
      <span class="brand__mark"></span>
      <span class="brand__name">Holloway's Bread</span>
    </div>
  </section>
</body>
</html>
```